Brindlow Engineering Business Card

our company has just rebranded and taken on a new logo design. We now need to update our business cards with the new logo. This is also an opportunity to reformat and modernize our look. We are an engineering company so the look needs to be formal and professional yet it should look modern. Have a look at our current card and the new card should have the same information.

Target Market(s)

Engineering firms, government, mining companies

Industry/Entity Type

Mechanical Engineering

Contact Information for Business Card

Requirements
Must have
• look professional and modern
Should not have
• should not include the office locations 'Brisbane, Sydney and Kuala Lumpur'
• you will find this on the example but it should not be included in these versions. please remove from your submissions and resubmit

```html
<!DOCTYPE html>
<html lang="en">
<head>
<meta charset="utf-8">
<title>Brindlow Engineering – Business Card</title>
<link rel="stylesheet" href="https://fonts.googleapis.com/css2?family=Saira:wght@400;500;700&display=swap">
<style>
  :root {
    --brand-blue: #3d49a4;
    --card-white: #ffffff;
    --card-shade: #eeeeef;
    --ink-dark: #3a3a3c;
    --ink-light: #ffffff;
    --page-bg: #e6e6e8;
  }
  * { margin: 0; padding: 0; box-sizing: border-box; }
  html, body {
    width: 1200px;
    height: 1085px;
    overflow: hidden;
    background: var(--page-bg);
    font-family: "Saira", sans-serif;
  }
  .card {
    position: absolute;
    left: 100px;
    top: 257px;
    width: 1000px;
    height: 570px;
    background: linear-gradient(135deg, var(--card-white) 40%, var(--card-shade) 100%);
    box-shadow: 0 18px 40px rgba(0,0,0,0.18);
    overflow: hidden;
  }
  .contact-panel {
    position: absolute;
    inset: 0;
    width: 1000px;
    height: 570px;
  }
  .contact-panel .wave { fill: var(--brand-blue); }
  .contact-panel .icon-ring { fill: none; stroke: var(--ink-light); stroke-width: 3; }
  .contact-panel .icon-glyph { fill: none; stroke: var(--ink-light); stroke-width: 2.6; stroke-linecap: round; stroke-linejoin: round; }
  .contact-panel .icon-solid { fill: var(--ink-light); }
  .contact-panel .icon-hole { fill: var(--brand-blue); }
  .contact-item {
    position: absolute;
    right: 622px;
    width: 320px;
    text-align: right;
    color: var(--ink-light);
    font-size: 25px;
    line-height: 1.22;
    font-weight: 400;
    letter-spacing: 0.5px;
    transform: translateY(-50%);
  }
  .contact-item.phone { top: 160px; }
  .contact-item.address { top: 295px; }
  .contact-item.web { top: 430px; }
  .brand {
    position: absolute;
    left: 560px;
    top: 118px;
    display: flex;
    align-items: center;
    gap: 18px;
  }
  .brand-dot {
    width: 58px;
    height: 58px;
    border-radius: 50%;
    border: 4px solid var(--brand-blue);
    flex: none;
  }
  .brand-name {
    color: var(--brand-blue);
    font-weight: 700;
    font-size: 34px;
    line-height: 1.05;
    letter-spacing: 2px;
    text-transform: uppercase;
  }
  .person {
    position: absolute;
    left: 640px;
    top: 300px;
    color: var(--ink-dark);
  }
  .person-name {
    font-size: 30px;
    font-weight: 500;
    letter-spacing: 1.5px;
    text-transform: uppercase;
  }
  .person-role {
    font-size: 25px;
    font-weight: 400;
    letter-spacing: 0.5px;
  }
</style>
</head>
<body>
  <main class="card">
    <svg class="contact-panel" viewBox="0 0 1000 570" aria-hidden="true">
      <path class="wave" d="
        M0,0 H405 V100
        C405,112 420,110 440,110
        C468,110 490,132 490,160
        C490,190 468,210 440,210
        C418,210 408,222 408,240
        C408,245 420,245 440,245
        C468,245 490,267 490,295
        C490,325 468,345 440,345
        C418,345 408,357 408,375
        C408,380 420,380 440,380
        C468,380 490,402 490,430
        C490,460 468,480 440,480
        C418,480 410,492 410,510
        V570 H0 Z"/>
      <circle class="icon-ring" cx="445" cy="160" r="24"/>
      <path class="icon-glyph" d="M436,149 c-3,0 -4,3 -3,7 c2,8 8,14 16,16 c4,1 7,0 7,-3 l-1,-3 l-5,-2 l-3,3 c-4,-2 -7,-5 -9,-9 l3,-3 l-2,-5 z"/>
      <circle class="icon-ring" cx="445" cy="295" r="24"/>
      <path class="icon-solid" d="M445,280 c-7,0 -12,5 -12,12 c0,8 12,19 12,19 c0,0 12,-11 12,-19 c0,-7 -5,-12 -12,-12 z"/>
      <circle class="icon-hole" cx="445" cy="292" r="4.5"/>
      <circle class="icon-ring" cx="445" cy="430" r="24"/>
      <circle class="icon-glyph" cx="445" cy="430" r="14"/>
      <ellipse class="icon-glyph" cx="445" cy="430" rx="6" ry="14"/>
      <path class="icon-glyph" d="M431,430 H459 M434,422 H456 M434,438 H456"/>
    </svg>

    <p class="contact-item phone">012 555 0147<br>012 555 0147</p>
    <p class="contact-item address">041.12th floor,<br>Harbour Crest Road<br>Norwood</p>
    <p class="contact-item web">mhale@brindlow.com<br>brindlowengineering.com</p>

    <div class="brand">
      <span class="brand-dot"></span>
      <span class="brand-name">Brindlow<br>Engineering</span>
    </div>

    <div class="person">
      <p class="person-name">Marcus Hale</p>
      <p class="person-role">Managing Director</p>
    </div>
  </main>
</body>
</html>
```